Vodka label for New Brand called KIRO Vodka

We need a label measuring 3.5 inches wide & 5 inches tall for this vodka bottle. The brand is "KIRO Vodka". This should be the largest font on the label. "Handcrafted in the USA" should be on bottle in small font near the bottom. The tagline "Keeping It Real Onward" also needs to be included anywhere that makes sense in a smaller font than the brand name. Also in smaller font at the bottom/corners- "80 proof, 750 ml, 40% alc/vol" I value the human mind over AI, but am providing a couple designs that were AI generated to give you a better idea where to start and what we are looking for. Thank you!

Target Market(s)

21-45 year olds.

Industry/Entity Type

Alcohol

Colors
0054AA
0677BA
7BADD7
CADEEF
E8F1F8
EB3D1F
EC4F4E
F09395
F8D3D4
FCEDEE

Requirements
Should not have
• You can not use the US flag but can use elements of it.

```html
<!DOCTYPE html>
<html lang="en">
<head>
<meta charset="utf-8">
<title>KIRO Vodka Label</title>
<link rel="stylesheet" href="https://fonts.googleapis.com/css2?family=Montserrat:wght@500;600;800&display=swap">
<style>
  :root {
    --navy: #012868;
    --crimson: #c00c30;
    --wine: #8a2a2d;
    --sky: #cddff0;
    --paper: #ffffff;
    --ink: #111111;
    --page: #ffffff;
  }
  html, body {
    margin: 0;
    padding: 0;
    width: 1200px;
    height: 1200px;
    overflow: hidden;
    background: var(--page);
  }
  .canvas {
    width: 1200px;
    height: 1200px;
    display: flex;
    align-items: center;
    justify-content: center;
  }
  .label {
    width: 738px;
    height: 1053px;
    display: block;
  }
  .label-field { fill: var(--navy); }
  .info-panel { fill: var(--paper); }
  .base-band { fill: var(--sky); }
  .panel-frame { fill: none; stroke: var(--crimson); stroke-width: 18; }
  .brand-name {
    font-family: "Montserrat", sans-serif;
    font-weight: 800;
    font-size: 205px;
    fill: var(--navy);
  }
  .brand-type {
    font-family: "Montserrat", sans-serif;
    font-weight: 600;
    font-size: 42px;
    fill: var(--wine);
  }
  .tagline {
    font-family: "Montserrat", sans-serif;
    font-weight: 500;
    font-size: 25px;
    fill: var(--navy);
  }
  .origin {
    font-family: "Montserrat", sans-serif;
    font-weight: 500;
    font-size: 24px;
    fill: var(--ink);
  }
  .origin-rule { stroke: var(--ink); stroke-width: 3; }
  .spec {
    font-family: "Montserrat", sans-serif;
    font-weight: 500;
    font-size: 18px;
    fill: var(--ink);
  }
</style>
</head>
<body>
<main class="canvas">
  <svg class="label" viewBox="127 299 922 1316" xmlns="http://www.w3.org/2000/svg" role="img" aria-label="KIRO Vodka label">
    <rect class="label-field" x="127" y="299" width="922" height="1316"/>

    <rect class="info-panel" x="285" y="562" width="606" height="738"/>
    <rect class="base-band" x="285" y="1108" width="606" height="192" role="img" aria-label="Pale blue decorative band behind the product details"/>
    <rect class="panel-frame" x="316" y="592" width="544" height="678"/>

    <text class="brand-name" x="588" y="955" text-anchor="middle" textLength="432" lengthAdjust="spacingAndGlyphs">KIRO</text>
    <text class="brand-type" x="590" y="1006" text-anchor="middle" letter-spacing="14">VODKA</text>
    <text class="tagline" x="588" y="1045" text-anchor="middle" textLength="432" lengthAdjust="spacingAndGlyphs">KEEPING IT REAL ONWARD</text>

    <text class="origin" x="588" y="1188" text-anchor="middle" textLength="380" lengthAdjust="spacingAndGlyphs">HANDCRAFTED IN THE USA</text>
    <line class="origin-rule" x1="382" y1="1197" x2="794" y2="1197"/>
    <text class="spec" x="588" y="1227" text-anchor="middle" textLength="313" lengthAdjust="spacingAndGlyphs">80 proof, 750 ml, 40% alc/vol</text>
  </svg>
</main>
</body>
</html>
```